Medical Cannabis company is looking for a LOGO design *

SILVER PETALWORKS (SP) is a new company in the Israeli medical cannabis industry. We will engage in PREMIUM medical cannabis growing and cultivation and also manufacturing of HIGH-END cannabis based medical products.
the design should reflect luxury, high-end and Pharma-grade products.
the design should use color GOLD and NOT using the famous cannabis leaf !

Target Market(s)

international medical cannabis Pharmaceutical companies
and of course local and international patients

Contact Information for Business Card

Yoav Ben-Ami
Founder and CEO

Silver Petalworks
Medical grade cannabis

yoavbenami@mailnest.example
972-52-3186907

Colors
ffc214
fbed22

Requirements
Must have
• clean and simple
• luxury
• gold !!
• (can also have green for Cannabis and/or blue for Pharma)
Should not have
• cannabis leaf

```html
<!DOCTYPE html>
<html lang="en">
<head>
<meta charset="utf-8">
<title>Silver Petalworks — Business Card</title>
<link href="https://fonts.googleapis.com/css2?family=Marcellus&family=Tinos:wght@400;700&family=Lato:wght@400&display=swap" rel="stylesheet">
<style>
  :root {
    --gold: #ffc214;
    --lemon: #f5ea22;
    --white: #ffffff;
    --ink: #111111;
    --page: #ffffff;
  }
  * { margin: 0; padding: 0; box-sizing: border-box; }
  html, body { width: 1200px; height: 1000px; overflow: hidden; background: var(--page); }
  .canvas { position: relative; width: 1200px; height: 1000px; }

  .card-front { position: absolute; left: 179px; top: 391px; width: 393px; height: 217px; background: var(--white); }
  .front-band {
    position: absolute; left: 0; top: 0; width: 393px; height: 137px;
    background: linear-gradient(90deg, var(--lemon) 0%, var(--gold) 38%, var(--gold) 62%, var(--lemon) 100%);
  }
  .brand { position: absolute; display: flex; align-items: center; gap: 14px; color: var(--white); }
  .brand-dot { width: 46px; height: 46px; border: 1.5px solid var(--white); border-radius: 50%; flex: none; }
  .brand-name { font-family: "Marcellus", serif; font-size: 19px; line-height: 1.35; letter-spacing: 0.5px; }
  .front-band .brand { left: 92px; top: 42px; }

  .holder { position: absolute; left: 60px; top: 160px; text-align: right; width: 132px; }
  .holder-name { font-family: "Tinos", serif; font-size: 24px; color: var(--ink); line-height: 1; white-space: nowrap; }
  .holder-role { font-family: "Lato", sans-serif; font-size: 7.5px; color: var(--ink); margin-top: 2px; }

  .divider { position: absolute; left: 259px; top: 143px; width: 1.5px; height: 75px; background: var(--gold); }

  .contacts { position: absolute; left: 274px; top: 153px; font-family: "Lato", sans-serif; font-size: 7.5px; color: var(--ink); }
  .contact { display: flex; align-items: flex-start; gap: 5px; line-height: 12px; }
  .contact + .contact { margin-top: 3px; }
  .contact svg { flex: none; margin-top: 1px; }

  .card-back { position: absolute; left: 662px; top: 391px; width: 382px; height: 217px; background: var(--gold); }
  .card-back .brand { left: 94px; top: 74px; }
  .back-email { position: absolute; left: 0; bottom: 4px; width: 100%; text-align: center; font-family: "Tinos", serif; font-weight: 700; font-size: 9.5px; color: var(--white); }
</style>
</head>
<body>
<div class="canvas">
  <section class="card-front">
    <div class="front-band">
      <div class="brand">
        <span class="brand-dot"></span>
        <span class="brand-name">SILVER<br>PETALWORKS</span>
      </div>
    </div>
    <div class="holder">
      <div class="holder-name">Yoav Ben-Ami</div>
      <div class="holder-role">Founder and CEO</div>
    </div>
    <div class="divider"></div>
    <div class="contacts">
      <div class="contact">
        <svg width="10" height="10" viewBox="0 0 10 10"><circle cx="5" cy="5" r="5" fill="#ffc214"/><path d="M2.6 5.2 5 3 7.4 5.2V7.3H2.6Z" fill="#111"/></svg>
        <span>Silver Petalworks<br>Medical grade cannabis</span>
      </div>
      <div class="contact">
        <svg width="10" height="10" viewBox="0 0 10 10"><circle cx="5" cy="5" r="5" fill="#ffc214"/><rect x="2.6" y="3.4" width="4.8" height="3.3" fill="#111"/><path d="M2.6 3.4 5 5.3 7.4 3.4" stroke="#ffc214" stroke-width="0.6" fill="none"/></svg>
        <span>yoavbenami@mailnest.example</span>
      </div>
      <div class="contact">
        <svg width="10" height="10" viewBox="0 0 10 10"><circle cx="5" cy="5" r="5" fill="#ffc214"/><rect x="3.4" y="2.4" width="3.2" height="5.2" rx="0.6" fill="#111"/></svg>
        <span>972-52-3186907</span>
      </div>
    </div>
  </section>

  <section class="card-back">
    <div class="brand">
      <span class="brand-dot"></span>
      <span class="brand-name">SILVER<br>PETALWORKS</span>
    </div>
    <div class="back-email">yoavbenami@mailnest.example</div>
  </section>
</div>
</body>
</html>
```